Design a web site for my business - Brellan Coatworks Mackaby.

We are a family business that handles design, fabrication and installation of powder coated aluminum, stainless steel and glass products. Including handrails, privacy slat screens, electric gates and pool fencing. We are based in the Whitsundays in North Queensland and service an area from Airlie Beach to Townsville.

Target Market(s)

Domestic and commercial

Industry/Entity Type

fabrication - manufacturing

Coding

Coded - Design and coding required

Number of Pages Required

5+ page

Colors
0054AA
0677BA
7BADD7
CADEEF
E8F1F8

Requirements
Must have
• photo galleries, contact page, one page for privacy screens, balustrades, glass fencing, stainless steel handrail, powder coated aluminium handrails and pool fencing

```html
<!DOCTYPE html>
<html lang="en">
<head>
<meta charset="utf-8">
<title>Brellan Coatworks Mackaby</title>
<link href="https://fonts.googleapis.com/css2?family=Montserrat:wght@600;700;800&family=Inter:wght@400;500;600;700&display=swap" rel="stylesheet">
<style>
:root{
  --backdrop:#8f8f8f;
  --ink:#111a22;
  --ink-soft:#5b6670;
  --dark:#111a22;
  --darker:#0e151c;
  --teal:#1d6a84;
  --teal-deep:#163f52;
  --gold:#d6a656;
  --light:#f3f5f7;
  --line:#e6eaee;
  --white:#ffffff;
}
*{box-sizing:border-box;margin:0;padding:0}
html,body{width:1200px;height:3272px;overflow:hidden}
body{background:var(--backdrop);font-family:"Inter",sans-serif;color:var(--ink)}
h1,h2,h3,.display{font-family:"Montserrat",sans-serif;font-weight:700;letter-spacing:-0.5px}
.page{position:absolute;left:85px;top:77px;width:1030px;height:3117px;background:var(--white);overflow:hidden}
section,header,footer{position:relative;width:1030px}
.eyebrow{font-size:7px;font-weight:700;letter-spacing:1.6px;text-transform:uppercase;color:var(--ink-soft)}

/* nav */
.nav{height:45px;background:#eef0f1;display:flex;align-items:center;justify-content:space-between;padding:0 140px}
.brand{display:flex;align-items:center;gap:8px}
.brand-mark{width:24px;height:24px;border-radius:5px;background:var(--teal)}
.brand-name{font-size:9px;font-weight:700;line-height:1.2}
.nav-links{display:flex;align-items:center;gap:16px;font-size:8px;font-weight:600}
.btn-dark{background:var(--dark);color:#fff;padding:7px 10px;border-radius:14px;font-size:8px;font-weight:700}

/* hero */
.hero{height:476px;background:linear-gradient(100deg,#1f5f78 0%,#2b6c80 45%,#6e7c7a 75%,#a87a5d 100%)}
.hero-photo{position:absolute;inset:0;background:linear-gradient(180deg,rgba(18,44,58,.2),rgba(30,40,45,.35))}
.hero-copy{position:absolute;left:140px;top:70px;width:430px;color:#fff}
.hero-copy .eyebrow{color:var(--gold)}
.hero-copy h1{font-size:42px;line-height:47px;margin-top:10px}
.hero-copy p{font-size:10px;line-height:16px;margin-top:18px;color:#e6eef1}
.hero-actions{display:flex;gap:8px;margin-top:18px}
.btn-gold{background:var(--gold);color:var(--ink);font-size:9px;font-weight:700;padding:9px 13px;border-radius:16px}
.btn-ghost{border:1px solid rgba(255,255,255,.6);color:#fff;font-size:9px;font-weight:600;padding:8px 12px;border-radius:16px}
.tags{display:flex;gap:8px;margin-top:14px}
.tags span{border:1px solid rgba(255,255,255,.5);font-size:7px;padding:5px 8px;border-radius:12px}
.hero-card{position:absolute;left:605px;top:112px;width:285px;height:305px;background:#fff;border-radius:14px;padding:14px}
.hero-card-top{display:flex;justify-content:space-between;font-size:7px;color:var(--ink-soft)}
.hero-card-top b{color:var(--teal)}
.thumb{height:67px;border-radius:8px;margin-top:8px}
.t1{background:linear-gradient(90deg,#2e2f31,#cfc7bc,#8a5a3a)}
.t2{background:linear-gradient(90deg,#3d4a4e,#6a8d9a,#b49272)}
.t3{background:linear-gradient(90deg,#7a5540,#a89d94,#405a3a)}
.hero-card p{font-size:8px;line-height:13px;margin-top:10px}

/* steps */
.steps{height:75px;background:var(--dark);display:flex;padding:0 140px}
.step{width:188px;border-right:1px solid #26313a;padding:22px 0 0 15px;color:#fff}
.step b{font-family:"Montserrat",sans-serif;font-size:15px;color:var(--gold);display:block}
.step span{font-size:8px;font-weight:600}

/* services */
.services{height:584px;text-align:center;padding-top:60px}
.services h2{font-size:28px;line-height:31px;margin:12px auto 0;width:400px}
.lede{font-size:8.5px;line-height:14px;color:var(--ink-soft);width:400px;margin:12px auto 0}
.service-grid{position:absolute;left:140px;top:236px;width:750px;display:grid;grid-template-columns:repeat(3,241px);gap:14px 13px;text-align:left}
.service-card{height:137px;border:1px solid var(--line);border-radius:12px;padding:18px;box-shadow:0 4px 12px rgba(0,0,0,.04)}
.icon-tile{width:26px;height:26px;border-radius:6px;background:#e3eef2;display:flex;align-items:center;justify-content:center}
.service-card h3{font-size:12px;margin-top:12px;letter-spacing:0}
.service-card p{font-size:8px;line-height:13px;color:var(--ink-soft);margin-top:6px}

/* why */
.why{height:419px;background:var(--light)}
.why-photo{position:absolute;left:140px;top:60px;width:337px;height:300px;border-radius:14px;background:linear-gradient(120deg,#2a2a2a 0%,#8a5a3a 35%,#d8d4cc 60%,#b08050 100%)}
.why-badge{position:absolute;left:366px;top:267px;width:128px;height:66px;background:#fff;border-radius:10px;padding:12px;box-shadow:0 6px 16px rgba(0,0,0,.12)}
.why-badge b{font-size:8px;display:block}
.why-badge span{font-size:7px;line-height:12px;color:var(--ink-soft);display:block;margin-top:5px}
.why-copy{position:absolute;left:518px;top:76px;width:380px}
.why-copy h2{font-size:27px;line-height:31px;margin-top:10px}
.why-copy .lede{margin:14px 0 0;text-align:left;width:370px}
.checks{list-style:none;margin-top:16px}
.checks li{font-size:8px;font-weight:600;display:flex;gap:10px;align-items:center;height:21px}
.link{font-size:8.5px;font-weight:700;color:var(--teal);margin-top:10px;display:block}

/* projects */
.projects{height:455px;text-align:center;padding-top:60px}
.projects h2{font-size:28px;line-height:31px;margin-top:12px}
.project-row{position:absolute;left:140px;top:166px;display:flex;gap:10px}
.project{width:180px;height:231px;border-radius:10px;position:relative;text-align:left}
.project span{position:absolute;left:12px;bottom:14px;font-family:"Montserrat",sans-serif;font-size:11px;font-weight:700;color:#fff}
.p1{background:linear-gradient(180deg,#3b3d40,#6d6f72 60%,#2b2c2e)}
.p2{background:linear-gradient(180deg,#5b6f7f,#2b2e2c 55%,#3c5a30)}
.p3{background:linear-gradient(180deg,#b8b8b6,#8a8680 55%,#3a3835)}
.p4{background:linear-gradient(180deg,#c9c7c2,#9a8470 55%,#3d4a5e)}

/* area */
.area{height:253px;background:linear-gradient(100deg,#1c6e8c,#1a4d63 60%,#12303f);color:#fff}
.area-copy{position:absolute;left:140px;top:54px;width:380px}
.area-copy .eyebrow{color:#d9e6ea}
.area-copy h2{font-size:28px;line-height:31px;margin-top:10px}
.area-copy p{font-size:8px;line-height:13px;margin-top:10px;color:#d9e6ea}
.chips{position:absolute;left:565px;top:95px;width:330px;display:flex;flex-wrap:wrap;gap:8px}
.chips span{font-size:8px;font-weight:600;border:1px solid rgba(255,255,255,.4);background:rgba(255,255,255,.08);padding:8px 10px;border-radius:14px}

/* cta */
.cta{height:232px;background:var(--dark);color:#fff;text-align:center;padding-top:44px}
.cta h2{font-size:28px;line-height:31px}
.cta p{font-size:8.5px;line-height:14px;color:#c7ced4;width:340px;margin:18px auto 0}
.cta .btn-gold{display:inline-block;margin-top:10px}

/* quote */
.quote{height:441px;background:#f6f7f9}
.quote-copy{position:absolute;left:140px;top:60px;width:340px}
.quote-copy h2{font-size:28px;line-height:31px;margin-top:10px}
.quote-copy p{font-size:8.5px;line-height:14px;color:var(--ink-soft);margin-top:12px}
.quote-info{margin-top:18px;background:#fff;border:1px solid var(--line);border-radius:10px;padding:12px 14px;font-size:8px;line-height:14px;color:var(--ink-soft);width:330px}
.quote-info b{color:var(--ink)}
.form{position:absolute;left:502px;top:61px;width:388px;height:320px;background:#fff;border-radius:14px;padding:20px 18px;box-shadow:0 10px 24px rgba(0,0,0,.08)}
.form label{display:block;font-size:7.5px;font-weight:700;margin-bottom:7px}
.field{height:27px;border:1px solid var(--line);border-radius:8px;background:#f4f6f8;font-size:7.5px;color:var(--ink-soft);padding:0 10px;display:flex;align-items:center;justify-content:space-between;margin-bottom:18px}
.field.area-field{height:70px;align-items:flex-start;padding-top:12px;margin-bottom:10px}
.field.select{color:var(--ink);background:#fff}
.submit{height:27px;border-radius:14px;background:var(--gold);font-size:8px;font-weight:700;display:flex;align-items:center;justify-content:center}

/* footer */
.footer{height:137px;background:var(--darker);color:#fff}
.foot-brand{position:absolute;left:140px;top:40px}
.foot-brand .brand-mark{width:24px;height:24px}
.foot-brand b{font-size:9px;display:block;margin-top:6px}
.foot-brand p{font-size:8px;color:#a9b2ba;margin-top:14px}
.foot-col{position:absolute;top:36px;font-size:8px;line-height:18px;color:#c7ced4}
.foot-col b{color:#fff;display:block}
</style>
</head>
<body>
<div class="page">

<header class="nav">
  <div class="brand"><div class="brand-mark"></div><div class="brand-name">Brellan Coatworks Mackaby</div></div>
  <nav class="nav-links"><span>Services</span><span>Our Work</span><span>About</span><span>Service Area</span><span class="btn-dark">Request Quote</span></nav>
</header>

<section class="hero">
  <div class="hero-photo" role="img" aria-label="Coastal mountain road winding through red rock country under a teal sky"></div>
  <div class="hero-copy">
    <div class="eyebrow">Family owned • North Queensland</div>
    <h1>Custom Aluminum, Stainless Steel &amp; Glass Solutions Built for Coastal Living</h1>
    <p>Design, fabrication and installation of powder coated aluminum, stainless steel and glass products across the Whitsundays, Airlie Beach and Townsville.</p>
    <div class="hero-actions"><span class="btn-gold">Request a Quote</span><span class="btn-ghost">Explore Services</span></div>
    <div class="tags"><span>Handrails</span><span>Privacy Screens</span><span>Electric Gates</span><span>Pool Fencing</span></div>
  </div>
  <div class="hero-card">
    <div class="hero-card-top"><span>Coastal-grade fabrication</span><b>Built to last</b></div>
    <div class="thumb t1" role="img" aria-label="Modern open-plan interior with timber wall"></div>
    <div class="thumb t2" role="img" aria-label="Resort pool framed by glass and slat screens"></div>
    <div class="thumb t3" role="img" aria-label="Brick family home with garage"></div>
    <p>Precision made for homes, resorts, commercial buildings and outdoor coastal spaces.</p>
  </div>
</section>

<section class="steps">
  <div class="step"><b>01</b><span>Custom Design</span></div>
  <div class="step"><b>02</b><span>Local Fabrication</span></div>
  <div class="step"><b>03</b><span>Professional Installation</span></div>
  <div class="step"><b>04</b><span>Durable Coastal Finish</span></div>
</section>

<section class="services">
  <div class="eyebrow">What we build</div>
  <h2>Complete fabrication and installation for modern properties</h2>
  <p class="lede">From privacy and safety to entrance appeal, every product is made to suit your property, finish, lifestyle and local coastal conditions.</p>
  <div class="service-grid">
    <div class="service-card"><div class="icon-tile"><svg width="10" height="10"><rect x="1" y="1" width="8" height="8" fill="#7fa9b8"/></svg></div><h3>Powder Coated Aluminum</h3><p>Custom aluminum work with durable powder coated finishes for long-lasting performance and a clean architectural look.</p></div>
    <div class="service-card"><div class="icon-tile"><svg width="10" height="10"><path d="M5 1 9 5 5 9 1 5Z" fill="none" stroke="#1d6a84"/></svg></div><h3>Stainless Steel Fabrication</h3><p>Strong, refined stainless steel solutions for homes, businesses and coastal environments.</p></div>
    <div class="service-card"><div class="icon-tile"><svg width="12" height="10"><path d="M3 2h8L9 8H1Z" fill="none" stroke="#1d6a84"/></svg></div><h3>Glass Pool Fencing</h3><p>Frameless and semi-frameless glass fencing that keeps pool areas safe while preserving open views.</p></div>
    <div class="service-card"><div class="icon-tile"><svg width="12" height="4"><path d="M0 2h12" stroke="#1d6a84"/></svg></div><h3>Handrails &amp; Balustrades</h3><p>Neat, safe and code-conscious handrail systems for stairs, balconies, decks and access areas.</p></div>
    <div class="service-card"><div class="icon-tile"><svg width="10" height="10"><rect x="1" y="1" width="8" height="8" fill="#7fa9b8"/></svg></div><h3>Privacy Slat Screens</h3><p>Modern slat screens for privacy, shade and separation without blocking the coastal outdoor feel.</p></div>
    <div class="service-card"><div class="icon-tile"><svg width="12" height="8"><path d="M1 4h10M3 2 1 4l2 2M9 2l2 2-2 2" fill="none" stroke="#1d6a84"/></svg></div><h3>Electric Gates</h3><p>Custom driveway gates designed for security, convenience and a strong first impression.</p></div>
  </div>
</section>

<section class="why">
  <div class="why-photo" role="img" aria-label="Open living room with timber feature wall opening to a deck"></div>
  <div class="why-badge"><b>Family Business</b><span>Local service from Airlie Beach to Townsville</span></div>
  <div class="why-copy">
    <div class="eyebrow">Why choose us</div>
    <h2>Built locally. Installed professionally. Made to handle North Queensland.</h2>
    <p class="lede">We combine practical design, reliable fabrication and careful installation to deliver products that look great and perform in real coastal conditions.</p>
    <ul class="checks">
      <li><svg width="8" height="8"><path d="M1 4l2 2 4-5" fill="none" stroke="#1d6a84" stroke-width="1.5"/></svg>Custom solutions designed around your property</li>
      <li><svg width="8" height="8"><path d="M1 4l2 2 4-5" fill="none" stroke="#1d6a84" stroke-width="1.5"/></svg>Powder coated aluminum, stainless steel and glass expertise</li>
      <li><svg width="8" height="8"><path d="M1 4l2 2 4-5" fill="none" stroke="#1d6a84" stroke-width="1.5"/></svg>Quality finish options for residential and commercial projects</li>
      <li><svg width="8" height="8"><path d="M1 4l2 2 4-5" fill="none" stroke="#1d6a84" stroke-width="1.5"/></svg>Friendly family-business service with local knowledge</li>
    </ul>
    <span class="link">Start your project →</span>
  </div>
</section>

<section class="projects">
  <div class="eyebrow">Project style</div>
  <h2>Clean lines, coastal durability<br>and precise installation</h2>
  <div class="project-row">
    <div class="project p1" role="img" aria-label="Dark modern bathroom with glass screen"><span>Glass Pool Fencing</span></div>
    <div class="project p2" role="img" aria-label="Modern home with slat screens beneath a large tree"><span>Privacy Slat Screens</span></div>
    <div class="project p3" role="img" aria-label="Minimal interior with glass balustrade stair"><span>Electric Gates</span></div>
    <div class="project p4" role="img" aria-label="Living room with timber staircase and balustrade"><span>Handrails &amp; Balustrades</span></div>
  </div>
</section>

<section class="area">
  <div class="area-copy">
    <div class="eyebrow">Service area</div>
    <h2>Proudly servicing the Whitsundays and North Queensland</h2>
    <p>Based in the Whitsundays, we work with homeowners, builders, property managers and businesses from Airlie Beach through to Townsville.</p>
  </div>
  <div class="chips"><span>Airlie Beach</span><span>Whitsundays</span><span>Bowen</span><span>Proserpine</span><span>Ayr</span><span>Townsville</span></div>
</section>

<section class="cta">
  <h2>Need a custom gate, fence,<br>screen or handrail?</h2>
  <p>Tell us about your project and we'll help you choose the right materials, finish and installation approach.</p>
  <span class="btn-gold">Get a Free Quote</span>
</section>

<section class="quote">
  <div class="quote-copy">
    <div class="eyebrow">Request a quote</div>
    <h2>Let’s build something strong, clean and made for your property.</h2>
    <p>Share a few details and our team will get back to you about your aluminum, stainless steel or glass project.</p>
    <div class="quote-info"><b>Service:</b> Whitsundays to Townsville<br><b>Specialties:</b> Fabrication &amp; installation</div>
  </div>
  <div class="form">
    <label>Name</label><div class="field">Your name</div>
    <label>Phone / Email</label><div class="field">Best contact details</div>
    <label>Project Type</label><div class="field select">Glass Pool Fencing<svg width="8" height="5"><path d="M1 1l3 3 3-3" fill="none" stroke="#111a22"/></svg></div>
    <label>Message</label><div class="field area-field">Tell us about your project</div>
    <div class="submit">Submit Enquiry</div>
  </div>
</section>

<footer class="footer">
  <div class="foot-brand"><div class="brand-mark"></div><b>Brellan Coatworks Mackaby</b><p>Custom aluminum, stainless steel and glass fabrication for North Queensland.</p></div>
  <div class="foot-col" style="left:526px"><b>Services</b>Pool Fencing<br>Electric Gates<br>Privacy Screens</div>
  <div class="foot-col" style="left:717px"><b>Area</b>Airlie Beach<br>Whitsundays<br>Townsville</div>
</footer>

</div>
</body>
</html>
```